Varnick Earthworks and Septic needs a flyer to submit to contractors to offer our services

I need a sleek profession one page full color high gloss document showcasing our services to give to Mobile Home Companies and contractors that need our services.

Target Market(s)

Home Builders. Mobile Home Salesmen. People Building new homes.

Industry/Entity Type

Construction

Font styles to use
Serif
Sans Serif

Requirements
Must have
• Phone Number. Email address. Logo. Services offered: Mobile Home Pads, Meter Pole Placement and Connection, Waterline Connection, On Site Septic System Installs
Should not have
• Jokes, Nothing trying to be cute

```html
<!DOCTYPE html>
<html lang="en">
<head>
<meta charset="utf-8">
<title>Varnick Earthworks and Septic – Contractor Flyer</title>
<link href="https://fonts.googleapis.com/css2?family=Barlow+Condensed:ital,wght@0,400;0,500;0,600;0,700;0,800;1,400;1,500;1,700;1,800&display=swap" rel="stylesheet">
<style>
  :root {
    --page: #ffffff;
    --sheet: #dcebf8;
    --brand-blue: #114a82;
    --brand-red: #d0202a;
    --ink: #222222;
    --white: #ffffff;
  }
  * { box-sizing: border-box; margin: 0; padding: 0; }
  html, body {
    width: 1200px; height: 1000px; overflow: hidden;
    background: var(--page);
    font-family: "Barlow Condensed", "Arial Narrow", sans-serif;
  }
  .flyer {
    position: absolute; left: 341px; top: 133px;
    width: 518px; height: 733px;
    background: var(--sheet);
    color: var(--ink);
  }
  .headline {
    position: absolute; left: 31px; top: 22px;
    font-weight: 800; font-style: italic;
    font-size: 42px; line-height: 47px; letter-spacing: -0.3px;
    color: var(--ink); white-space: nowrap;
  }
  .headline .accent-blue { color: var(--brand-blue); }
  .headline .accent-red { color: var(--brand-red); }
  .region-tag {
    position: absolute; left: 31px; top: 175px;
    width: 219px; height: 30px;
    background: var(--brand-blue); color: var(--white);
    font-size: 17px; font-weight: 500; white-space: nowrap;
    display: flex; align-items: center; justify-content: center;
  }
  .services { position: absolute; left: 267px; top: 0; width: 240px; }
  .service { position: absolute; left: 0; width: 240px; }
  .service h2 {
    font-size: 17px; font-weight: 500; color: var(--brand-blue);
    line-height: 20px; white-space: nowrap;
  }
  .service p {
    font-size: 10.5px; font-style: italic; line-height: 12.5px;
    color: var(--ink); margin-top: 1px; white-space: nowrap;
  }
  .photo { position: absolute; }
  .photo.dig { left: 31px; top: 243px; width: 147px; height: 196px; background: linear-gradient(180deg, #5d7a45 0%, #b5895a 35%, #a97b4c 100%); }
  .photo.lot { left: 186px; top: 243px; width: 147px; height: 110px; background: linear-gradient(180deg, #a99a7a 0%, #b3603e 55%, #a4563a 100%); }
  .photo.irrigation { left: 341px; top: 243px; width: 147px; height: 196px; background: linear-gradient(180deg, #7fa0cf 0%, #9b8d78 35%, #6d5642 100%); }
  .photo.tank-lift { left: 31px; top: 447px; width: 147px; height: 110px; background: linear-gradient(180deg, #2f63b8 0%, #6d96cf 55%, #7b9a4e 100%); }
  .photo.home-set { left: 186px; top: 361px; width: 147px; height: 196px; background: linear-gradient(180deg, #6f9ad2 0%, #c9c9cc 40%, #b49a78 70%, #a78c6a 100%); }
  .photo.excavator { left: 341px; top: 447px; width: 147px; height: 110px; background: linear-gradient(180deg, #4f7fc3 0%, #7b8d58 35%, #c8a27a 100%); }
  .brand-name {
    position: absolute; left: 31px; top: 620px; width: 230px;
    display: flex; align-items: center; gap: 10px;
    font-size: 27px; font-weight: 800; line-height: 29px;
    color: var(--brand-blue); text-transform: uppercase; white-space: nowrap;
  }
  .brand-name .mark { flex: 0 0 20px; height: 20px; background: var(--brand-blue); }
  .counties { position: absolute; left: 340px; top: 596px; width: 148px; }
  .county-row { display: flex; gap: 3px; margin-bottom: 3px; }
  .county {
    height: 15px; background: var(--brand-blue); color: var(--white);
    font-size: 12px; font-weight: 500; line-height: 15px;
    text-align: center; flex-grow: 1; white-space: nowrap;
  }
  .contact { position: absolute; left: 340px; top: 655px; width: 160px; }
  .contact-line { display: flex; align-items: center; gap: 7px; white-space: nowrap; }
  .contact-line.phone {
    color: var(--brand-red); font-size: 15px; font-weight: 700; font-style: italic;
    height: 18px;
  }
  .contact-line.small {
    color: var(--brand-blue); font-size: 10px; font-style: italic;
    margin-top: 2px; padding-left: 3px; gap: 5px; height: 13px;
  }
  .contact-line svg { flex: 0 0 auto; }
</style>
</head>
<body>
  <main class="flyer">
    <h1 class="headline">
      <span class="accent-blue">Expert</span> Mobile<br>
      Home Services<br>
      You Can <span class="accent-red">Trust</span>
    </h1>
    <div class="region-tag">Excavating Services in East Texas</div>

    <section class="services">
      <div class="service" style="top:28px">
        <h2>Mobile Home Pads</h2>
        <p>Durable and stable pad installations for mobile homes.</p>
      </div>
      <div class="service" style="top:71px">
        <h2>Meter Pole Placement and Connection</h2>
        <p>Professional meter pole placement and reliable<br>electrical connections.</p>
      </div>
      <div class="service" style="top:128px">
        <h2>Waterline Connection</h2>
        <p>Efficient and secure waterline connections for new homes.</p>
      </div>
      <div class="service" style="top:172px">
        <h2>On Site Septic System Installs</h2>
        <p>Comprehensive septic system installations for your property.</p>
      </div>
    </section>

    <div class="photo dig" role="img" aria-label="Excavator digging a septic trench beside a mobile home"></div>
    <div class="photo lot" role="img" aria-label="Finished red-dirt lot with septic lids in front of a mobile home"></div>
    <div class="photo irrigation" role="img" aria-label="Spray field watering freshly graded soil near a power pole"></div>
    <div class="photo tank-lift" role="img" aria-label="Concrete septic tank being lifted by a boom truck over a field"></div>
    <div class="photo home-set" role="img" aria-label="Mobile home set on a graded pad with septic risers"></div>
    <div class="photo excavator" role="img" aria-label="Compact excavator beside an installed septic tank"></div>

    <div class="brand-name"><span class="mark"></span><span>Varnick Earthworks<br>&amp; Septic</span></div>

    <div class="counties">
      <div class="county-row">
        <span class="county" style="flex-basis:31px">Ellis</span>
        <span class="county" style="flex-basis:54px">Anderson</span>
        <span class="county" style="flex-basis:54px">Navarro</span>
      </div>
      <div class="county-row">
        <span class="county" style="flex-basis:50px">Henderson</span>
        <span class="county" style="flex-basis:43px">Kaufman</span>
        <span class="county" style="flex-basis:46px">Van Zandt</span>
      </div>
      <div class="county-row">
        <span class="county" style="flex-basis:33px">Smith</span>
        <span class="county" style="flex-basis:50px">Cherokee</span>
        <span class="county" style="flex-basis:56px">Limestone</span>
      </div>
    </div>

    <div class="contact">
      <div class="contact-line phone">
        <svg width="13" height="13" viewBox="0 0 24 24" aria-hidden="true"><path fill="#114a82" d="M6.6 10.8a15.1 15.1 0 0 0 6.6 6.6l2.2-2.2a1 1 0 0 1 1-.25 11.4 11.4 0 0 0 3.6.57 1 1 0 0 1 1 1V20a1 1 0 0 1-1 1A17 17 0 0 1 3 4a1 1 0 0 1 1-1h3.5a1 1 0 0 1 1 1c0 1.250.2 2.450.57 3.570a1 1 0 0 1-.25 1z"/></svg>
        <span>(903) 555-0147</span>
      </div>
      <div class="contact-line small">
        <svg width="8" height="6" viewBox="0 0 16 12" aria-hidden="true"><rect width="16" height="12" rx="1" fill="#114a82"/><path d="M1 1l7 5 7-5" stroke="#dcebf8" stroke-width="1.6" fill="none"/></svg>
        <span>dale@varnickearthworks.com</span>
      </div>
      <div class="contact-line small">
        <svg width="7" height="7" viewBox="0 0 12 12" aria-hidden="true"><circle cx="6" cy="6" r="6" fill="#114a82"/><path d="M0.5 6h11M6 0.5c-2.5 3-2.5 8 0 11M6 0.5c2.5 3 2.5 8 0 11" stroke="#dcebf8" stroke-width="1" fill="none"/></svg>
        <span>varnickearthworks.com</span>
      </div>
    </div>
  </main>
</body>
</html>
```